TKR Engineering Pty Ltd

I have already had nox welding and fabrication cards made , my business has changed too TKR engineering Pty Ltd so I need my logo changed on the cards
one side have my logo then the other side have what we do.
front side logo and details
owner /operator : Curtis Halvorsen
email: tkr.works@examplemail.net
number: 0491537204
ABN: 52 604 381 927
ACN: 728 391 056
on back have in dot points what we do:
* structural steel erection
* precast panels
* site welding
*steel alteration & repair
* rigging & dogging
*labour hire
Contact Information for Business Card
all details in breif
Look and feel
Each slider illustrates characteristics of the customer's brand and the style your logo design should communicate.

```html
<!DOCTYPE html>
<html lang="en">
<head>
<meta charset="utf-8">
<title>TKR Engineering Pty Ltd – Business Cards</title>
<link href="https://fonts.googleapis.com/css2?family=Roboto:wght@400;500;700;900&display=swap" rel="stylesheet">
<style>
  :root {
    --backdrop: #26272a;
    --navy: #0f1c2b;
    --paper: #f4f4f2;
    --ink: #14233a;
    --accent: #9a3a30;
    --muted: #3a3f47;
    --white: #ffffff;
  }
  * { box-sizing: border-box; margin: 0; padding: 0; }
  html, body {
    width: 1200px; height: 874px; overflow: hidden;
    background: var(--backdrop);
    font-family: "Roboto", Arial, sans-serif;
  }
  .canvas {
    width: 1200px; height: 874px;
    display: flex; flex-direction: column; align-items: center; justify-content: center;
    gap: 48px;
  }
  .card {
    position: relative;
    width: 600px; height: 343px;
    border-radius: 22px;
    overflow: hidden;
    box-shadow: 0 14px 30px rgba(0,0,0,.45);
  }

  /* Brand block */
  .brand {
    position: absolute;
    display: flex; flex-direction: column;
  }
  .brand__row { display: flex; align-items: center; gap: 12px; white-space: nowrap; }
  .brand__mark {
    width: 16px; height: 16px; border-radius: 50%;
    background: var(--accent); flex: none;
  }
  .brand__name {
    font-weight: 900; font-size: 30px; letter-spacing: .5px;
    text-transform: uppercase; line-height: 1;
  }
  .brand__phone {
    font-weight: 700; font-size: 15px; letter-spacing: 1px; margin-top: 16px;
  }

  /* Back: services */
  .card--services { background: var(--navy); color: var(--white); }
  .card--services .brand { top: 104px; left: 0; right: 0; align-items: center; }
  .card--services .brand__name,
  .card--services .brand__phone { color: var(--white); }

  .services {
    position: absolute; top: 212px; left: 0; right: 0;
    list-style: none; text-align: center;
    font-size: 17px; line-height: 30px;
  }
  .services li { display: inline; }
  .services li + li::before {
    content: ""; display: inline-block;
    width: 6px; height: 6px; border-radius: 50%;
    background: var(--accent); margin: 0 12px 3px;
  }
  .services .row-break { display: block; height: 0; }

  /* Front: contact */
  .card--contact { background: var(--paper); color: var(--ink); }
  .rule {
    position: absolute; top: 63px; left: 52px; width: 140px;
    height: 1.5px; background: var(--ink);
  }
  .card--contact .brand { top: 52px; right: 36px; align-items: flex-end; }
  .card--contact .brand__row { gap: 10px; }
  .card--contact .brand__name { font-size: 22px; color: var(--ink); }
  .card--contact .brand__mark { width: 13px; height: 13px; }
  .card--contact .brand__phone { color: var(--accent); font-size: 13px; margin-top: 8px; }

  .person { position: absolute; left: 52px; top: 176px; }
  .person__name { font-weight: 700; font-size: 24px; color: var(--ink); }
  .person__role { font-size: 16px; color: var(--accent); margin-top: 2px; }

  .contact-list {
    position: absolute; left: 52px; top: 248px;
    list-style: none; font-size: 16px; color: var(--muted); line-height: 26px;
  }
  .contact-list li { display: flex; align-items: center; gap: 10px; }
  .contact-list svg { width: 14px; height: 14px; fill: var(--ink); flex: none; }

  .divider {
    position: absolute; left: 300px; top: 252px;
    width: 1.5px; height: 46px; background: var(--muted);
  }
  .registration {
    position: absolute; left: 322px; top: 252px;
    font-size: 16px; line-height: 24px; color: var(--muted);
  }
</style>
</head>
<body>
<main class="canvas">

  <section class="card card--services" aria-label="Card back: services">
    <div class="brand">
      <div class="brand__row">
        <span class="brand__mark"></span>
        <span class="brand__name">TKR Engineering Pty Ltd</span>
      </div>
      <div class="brand__phone">0491537204</div>
    </div>
    <ul class="services">
      <li>Structural steel erection</li><li>Precast panels</li><li>Site welding</li>
      <span class="row-break"></span>
      <li>Steel alteration &amp; repair</li><li>Rigging &amp; dogging</li><li>Labour hire</li>
    </ul>
  </section>

  <section class="card card--contact" aria-label="Card front: contact details">
    <div class="rule"></div>
    <div class="brand">
      <div class="brand__row">
        <span class="brand__mark"></span>
        <span class="brand__name">TKR Engineering Pty Ltd</span>
      </div>
      <div class="brand__phone">0491537204</div>
    </div>

    <div class="person">
      <p class="person__name">Curtis Halvorsen</p>
      <p class="person__role">owner /operator</p>
    </div>

    <ul class="contact-list">
      <li>
        <svg viewBox="0 0 24 24" aria-hidden="true"><path d="M6.6 10.8a15.1 15.1 0 0 0 6.6 6.6l2.2-2.2c.3-.3.7-.4 1-.2 1.1.4 2.3.6 3.6.6.6 0 1 .4 1 1V20c0 .6-.4 1-1 1A17 17 0 0 1 3 4c0-.6.4-1 1-1h3.5c.6 0 1 .4 1 1 0 1.3.2 2.5.6 3.6.1.3 0 .7-.2 1z"/></svg>
        0491537204
      </li>
      <li>
        <svg viewBox="0 0 24 24" aria-hidden="true"><path d="M2 5h20v2l-10 7L2 7z"/><path d="M2 9l10 7 10-7v10H2z"/></svg>
        tkr.works@examplemail.net
      </li>
    </ul>

    <div class="divider"></div>
    <div class="registration">
      <p>ABN: 52 604 381 927</p>
      <p>ACN: 728 391 056</p>
    </div>
  </section>

</main>
</body>
</html>
```